Business Improvement Consultancy needs web design

I need a web design for my company, that offers support to manufacturing and distribution businesses.

We have worked with a range of organisations to help them get more out of their operational processes and supply chains.

With full end to end supply chain knowledge we help them identify waste in their supply chains that often get overlooked.

We support through a number of offerings

Developing an end to end supply chain strategy

Applying Lean to support the strategy

Interim support network to deliver quick wins and rapid cost improvement

Project Management

Interactive training tools for delivering supply chain best practice.

I have the logos done already, so it is more about look and feel, and the colour schemes etc giving a professional feel.

Also have the web domains www.veltrosiga.co, www.veltrosiga.co.uk & www.veltrosiga.eu, using Q&Q starter bundle

Target Market(s)

Manufacturing and distribution businesses, potentially other consultancies looking for collaboration

Industry/Entity Type

Business

Requirements
Must have
• Some pictures on related to performance improvement, bar charts showing productivity growth / increase.

Should have the chatterbox quipper and worknodes logos to share the website

```html
<!DOCTYPE html>
<html lang="en">
<head>
<meta charset="utf-8">
<title>Veltrosiga Europe – Home</title>
<link href="https://fonts.googleapis.com/css2?family=Lato:wght@400;700&family=Tenor+Sans&display=swap" rel="stylesheet">
<style>
:root{
  --ink:#25206a;
  --ink-soft:#4b4790;
  --text:#333;
  --nav-text:#8c8c8c;
  --rule:#cfcfcf;
  --footer:#a9a9a9;
  --white:#fff;
}
*{box-sizing:border-box;margin:0;padding:0}
html,body{width:1200px;height:1112px;overflow:hidden;background:var(--white)}
body{position:relative;font-family:"Lato",sans-serif;color:var(--text)}
.top-band{position:absolute;left:0;top:0;width:1200px;height:7px;background:var(--footer)}
.brand{position:absolute;left:145px;top:54px;display:flex;align-items:center;gap:14px}
.brand-dot{width:28px;height:28px;border-radius:50%;background:var(--ink-soft)}
.brand-name{font-family:"Tenor Sans",sans-serif;font-size:25px;color:var(--ink);white-space:nowrap}
.social{position:absolute;top:47px;left:848px;display:flex;gap:17px}
.social a{display:block;width:56px;height:56px;border-radius:8px}
.social .worknodes{background:#1b7fb0}
.social .chatterbox{background:#3b5aa3}
.social .quipper{background:#7fc6ea;border-radius:50%}
.main-nav{position:absolute;left:134px;top:141px;width:947px;height:49px;background:linear-gradient(#efefef,#dedede);display:flex;align-items:center}
.main-nav a{font-family:"Tenor Sans",sans-serif;font-size:16px;color:var(--nav-text);text-decoration:none;text-align:center;border-left:1px solid #c8c8c8;line-height:32px;white-space:nowrap}
.main-nav a.current{height:56px;line-height:56px;align-self:flex-start;background:linear-gradient(#4f4b93,#2e2975);color:var(--white);border:none;font-weight:700;font-family:"Lato",sans-serif;width:155px}
.main-nav a.first{border-left:none}
.hero{position:absolute;left:134px;top:218px;width:947px;height:368px;border:1px solid var(--rule);background:linear-gradient(110deg,#dfe9f0 0%,#b8cfdc 40%,#3e7c92 65%,#1f566b 85%,#6d9fb3 100%)}
.hero-card{position:absolute;left:12px;top:20px;width:502px;height:330px;border:3px solid var(--ink-soft);background:rgba(255,255,255,.8);padding:0 14px}
.hero-title{display:flex;align-items:center;gap:10px;margin:28px 0 22px 2px}
.hero-title .dot{flex:none;width:18px;height:18px;border-radius:50%;background:var(--ink)}
.hero-title h1{font-family:"Tenor Sans",sans-serif;font-size:22px;font-weight:400;color:var(--ink);white-space:nowrap}
.hero-card p{font-size:12.5px;font-weight:700;line-height:16.5px;color:#111;margin-bottom:16px}
.read-more{position:absolute;left:384px;top:290px;width:102px;height:31px;background:var(--ink-soft);color:var(--white);font-family:"Tenor Sans",sans-serif;font-size:15px;line-height:31px;text-align:center;text-decoration:none}
h2{font-family:"Tenor Sans",sans-serif;font-weight:700;font-size:23px;color:var(--ink);letter-spacing:.3px;white-space:nowrap}
.welcome{position:absolute;left:135px;top:622px;width:605px}
.welcome p{font-size:12.5px;line-height:16.5px;margin-top:16px}
.welcome h2+p{margin-top:24px}
.team-photo{position:absolute;left:134px;top:821px;width:220px;height:168px;border:1px solid #999;background:linear-gradient(160deg,#e9edf2,#b9c4d0 50%,#2c3550)}
.offer{position:absolute;left:381px;top:819px;width:370px}
.offer h3{font-size:12.5px;font-weight:700;color:var(--ink);line-height:16.5px;margin-bottom:9px}
.offer ul{list-style:none}
.offer li{font-size:12.5px;line-height:16px;margin-bottom:17px;padding-left:9px;text-indent:-9px}
.divider{position:absolute;left:763px;top:625px;width:1px;height:378px;background:var(--rule)}
.news{position:absolute;left:791px;top:622px;width:290px}
.news-item{position:absolute;left:0;width:290px}
.date{position:absolute;left:0;top:0;width:68px;height:69px;background:linear-gradient(#f2f2f2,#9b9b9b);border:1px solid #888;text-align:center;font-family:"Tenor Sans",sans-serif;font-size:18px;line-height:23px;color:#222;padding-top:14px}
.date::before{content:"";position:absolute;left:31px;top:3px;width:6px;height:6px;border-radius:50%;background:#fff;border:1px solid #777}
.news-item h4{position:absolute;left:85px;top:-2px;font-size:12.5px;font-weight:700;color:var(--ink);white-space:nowrap}
.news-item p{position:absolute;left:85px;top:21px;width:205px;font-size:12.5px;line-height:16.5px}
footer{position:absolute;left:0;top:1025px;width:1200px;height:87px;background:var(--footer);border-top:2px solid #888;text-align:center;font-size:13px;color:#111;padding-top:18px;line-height:21.5px}
footer a{color:#111;text-decoration:none}
</style>
</head>
<body>
<div class="top-band"></div>
<header>
  <div class="brand"><span class="brand-dot"></span><span class="brand-name">Veltrosiga Europe</span></div>
  <div class="social">
    <a class="worknodes" href="#" aria-label="Share on worknodes"></a>
    <a class="chatterbox" href="#" aria-label="Share on chatterbox"></a>
    <a class="quipper" href="#" aria-label="Share on quipper"></a>
  </div>
</header>
<nav class="main-nav">
  <a class="current" href="#">Home</a>
  <a class="first" href="#" style="width:155px">About Us</a>
  <a href="#" style="width:161px">Consultancy</a>
  <a href="#" style="width:124px">Interim</a>
  <a href="#" style="width:222px">Project Management</a>
  <a href="#" style="width:130px">Contact Us</a>
</nav>
<section class="hero" role="img" aria-label="Glass office tower with a rising productivity bar chart and arrow">
  <div class="hero-card">
    <div class="hero-title"><span class="dot"></span><h1>Veltrosiga - to improve, to enhance</h1></div>
    <p>Welcome to Veltrosiga Europe. We have worked with a range of organisations to help them get more out of their operational processes and supply chains.</p>
    <p>With full end to end supply chain knowledge we can help you identify waste in your supply chains that often get overlooked.</p>
    <p>Before you look to embark on cost reduction plans or a lean journey, get in touch to ensure that your chosen path delivers sustainability and profitable growth.</p>
    <p>It was popularised in the 1960s with the release of Presswell sheets containing Lorem Ipsum passages.</p>
    <a class="read-more" href="#">Read More</a>
  </div>
</section>
<section class="welcome">
  <h2>WELCOME TO VELTROSIGA</h2>
  <p>Lorem Ipsum is simply dummy text of the printing and typesetting industry. Lorem Ipsum has been the industry's standard dummy text ever since the 1500s, when an unknown printer took a galley of type and scrambled it to make a type specimen book. It has survived not only five centuries, but also the leap into electronic typesetting, remaining essentially unchanged.</p>
  <p>It was popularised in the 1960s with the release of Presswell sheets containing Lorem Ipsum passages, and more recently with desktop publishing software like Folio LayoutDesk including versions of Lorem Ipsum.</p>
</section>
<div class="team-photo" role="img" aria-label="Photo of a smiling business team in suits"></div>
<section class="offer">
  <h3>Please click on the above tabs for more details on how we can help with:</h3>
  <ul>
    <li>- Developing an end to end supply chain strategy</li>
    <li>- Applying Lean to support the strategy</li>
    <li>- Interim support network to deliver quick wins and rapid cost improvement</li>
    <li>- Project Management</li>
  </ul>
</section>
<div class="divider"></div>
<section class="news">
  <h2>LATEST NEWS</h2>
  <article class="news-item" style="top:51px"><div class="date">16<br>SEPT</div><h4>Lorem Ipsum is simply</h4><p>Lorem Ipsum is simply dummy text of the printing and typesetting industry. Lorem Ipsum has ...</p></article>
  <article class="news-item" style="top:137px"><div class="date">16<br>SEPT</div><h4>Lorem Ipsum is simply</h4><p>Lorem Ipsum is simply dummy text of the printing and typesetting industry. Lorem Ipsum has ...</p></article>
  <article class="news-item" style="top:224px"><div class="date">16<br>SEPT</div><h4>Lorem Ipsum is simply</h4><p>Lorem Ipsum is simply dummy text of the printing and typesetting industry. Lorem Ipsum has ...</p></article>
  <article class="news-item" style="top:310px"><div class="date">16<br>SEPT</div><h4>Lorem Ipsum is simply</h4><p>Lorem Ipsum is simply dummy text of the printing and typesetting industry. Lorem Ipsum has ...</p></article>
</section>
<footer>
  <div><a href="#">Home</a> &nbsp;|&nbsp; <a href="#">About Us</a> &nbsp;|&nbsp; <a href="#">Consultancy</a> &nbsp;|&nbsp; <a href="#">Interim</a> &nbsp;|&nbsp; <a href="#">Project Management</a> &nbsp;|&nbsp; <a href="#">Contact Us</a></div>
  <div>Veltrosiga Europe, PO Box 2087 Dunmere, Europe. E-mail: hello@veltrosiga.eu</div>
  <div>Copyright © 2011 all rights reserved, privacy policy.</div>
</footer>
</body>
</html>
```